Business cards design on a high standard

We advise clients on insurance and financial matters, since these clients pay for our advice, the design should have a high standard. Our logo should be included. From the colors we are open for everything.

Colors

Designer to choose colors to be used in the design.

```html
<!DOCTYPE html>
<html lang="en">
<head>
<meta charset="utf-8">
<title>Keller Advisory – Stationery</title>
<link href="https://fonts.googleapis.com/css2?family=Arimo:wght@400;700&family=Montserrat:wght@400;700&family=Quicksand:wght@400;500&display=swap" rel="stylesheet">
<style>
:root{
  --red:#c81e24;
  --grey:#8a8a8c;
  --black:#1b1b1c;
  --paper:#e8e8e8;
  --ink:#7a7a7a;
  --ink-dark:#222;
  --stage:#d2d2d2;
  --white:#f4f4f4;
}
*{margin:0;padding:0;box-sizing:border-box}
html,body{width:1200px;height:891px;overflow:hidden}
body{background:var(--stage);position:relative;font-family:"Arimo",Arial,sans-serif}

.letterhead{position:absolute;left:52px;top:74px;width:579px;height:742px;background:var(--paper);overflow:hidden;box-shadow:0 10px 18px rgba(0,0,0,.18)}
.footer-band{position:absolute;left:0;right:0;bottom:0;height:92px;background:linear-gradient(180deg,var(--grey) 0%,#3a3a3b 45%,var(--black) 100%)}
.brand{position:absolute;font-family:"Montserrat",sans-serif;font-weight:700;color:var(--red);line-height:1;text-transform:uppercase}
.brand .name{display:block}
.brand .sub{display:block;letter-spacing:.32em}
.letterhead .brand{left:31px;top:30px}
.letterhead .brand .name{font-size:40px;letter-spacing:.02em}
.letterhead .brand .sub{font-size:16px;margin-top:2px;padding-left:46px}

.lh-contact{position:absolute;left:437px;top:22px;font-family:"Quicksand",sans-serif;font-size:8.5px;color:var(--ink);line-height:11.3px}
.lh-contact .addr{margin-bottom:12px}
.lh-contact li{list-style:none;display:flex;align-items:center;gap:5px}
.ico{display:inline-block;width:8px;height:8px;border-radius:50%;background:var(--red);flex:none}
.hl{color:var(--red)}

.subject{position:absolute;left:176px;top:179px;font-size:9.5px;color:var(--ink)}
.date{position:absolute;left:481px;top:177px;font-size:9.5px;color:var(--ink)}
.label{display:block;color:var(--ink-dark);font-weight:700;margin-bottom:2px}
.greeting{position:absolute;left:176px;top:254px;font-size:12px;color:var(--ink)}
.letter-body{position:absolute;left:176px;top:281px;width:353px;font-size:8.4px;line-height:12.35px;color:var(--ink);text-align:justify}
.letter-body p{margin-bottom:12.3px}
.sidebar{position:absolute;left:51px;top:313px;width:80px;text-align:right;font-size:8.8px;line-height:12.2px;color:var(--ink)}
.sidebar p{margin-bottom:7px}
.sidebar .lead{color:var(--ink-dark)}
.signature{position:absolute;left:176px;top:546px;font-size:12px;line-height:14.5px;color:var(--ink)}

.card{position:absolute;left:681px;width:452px;height:262px;border-radius:26px;overflow:hidden;box-shadow:0 12px 16px rgba(0,0,0,.16)}
.card-front{top:156px;background:var(--paper)}
.card-back{top:470px;background:var(--black)}
.card-front .footer-band{height:124px;background:linear-gradient(180deg,#3a3a3b 0%,var(--black) 40%)}
.card-front .brand{left:22px;top:22px}
.card-front .brand .name{font-size:48px;letter-spacing:.02em}
.card-front .brand .sub{font-size:19px;margin-top:2px;padding-left:58px}
.card-back .brand{left:0;right:0;top:110px;text-align:center;color:#303031}
.card-back .brand .name{font-size:52px;letter-spacing:.02em}
.card-back .brand .sub{font-size:20px;margin-top:2px;padding-left:60px}

.card-contact{position:absolute;right:20px;top:148px;font-family:"Quicksand",sans-serif;font-size:11px;color:var(--white);text-align:right;line-height:15px}
.card-contact .addr{margin-bottom:9px}
.card-contact li{list-style:none;display:flex;justify-content:flex-end;align-items:center;gap:8px;line-height:14.7px}
.card-contact .ico{width:10px;height:10px}
.holder{position:absolute;left:22px;top:209px;font-family:"Montserrat",sans-serif}
.holder .person{font-weight:700;font-size:14.5px;color:var(--red);text-transform:uppercase;display:block}
.holder .role{font-family:"Quicksand",sans-serif;font-size:11px;color:var(--white);display:block;margin-top:1px}
</style>
</head>
<body>

<section class="letterhead">
  <div class="footer-band" role="img" aria-label="Decorative red, grey and black wave band along the page foot"></div>

  <div class="brand"><span class="name">Keller</span><span class="sub">Advisory</span></div>

  <div class="lh-contact">
    <div class="addr">P.O. Box 4120 Meridian<br>Idaho 83642</div>
    <ul>
      <li><span class="ico"></span><span>000 0000 00 00</span></li>
      <li><span class="ico"></span><span>000 0000 00 00</span></li>
      <li><span class="ico"></span><span>info@kelleradvisory.com</span></li>
      <li><span class="ico"></span><span>www.<span class="hl">kelleradvisory</span>.com</span></li>
    </ul>
  </div>

  <div class="subject"><span class="label">SUBJECT :</span>Lorem Ipsum is simply dummy</div>
  <div class="date"><span class="label">DATE :</span>15-09-2017</div>

  <div class="greeting">Dear Person,</div>

  <div class="letter-body">
    <p>Lorem Ipsum is simply dummy text of the printing and typesetting industry. Lorem Ipsum has been the industry's standard dummy text ever since the 1500s, when an unknown printer took a galley of type and scrambled it to make a type specimen book. It has survived not only five centuries, but also the leap into electronic typesetting, remaining essentially unchanged. It was popularised in the 1960s with the release of Tesselin sheets containing Lorem Ipsum passages, and more recently with desktop publishing software like Norvel PageKit including versions of Lorem Ipsum.</p>
    <p>Lorem Ipsum is simply dummy text of the printing and typesetting industry. Lorem Ipsum has been the industry's standard dummy text ever since the 1500s, when an unknown printer took a galley of type and scrambled it to make a type specimen book. It has survived not only five centuries, but also the leap into electronic typesetting, remaining essentially unchanged. It was popularised in the 1960s with the release of</p>
    <p>Tesselin sheets containing Lorem Ipsum passages, and more recently with desktop publishing software like Norvel PageKit including versions of Lorem Ipsum.lease of Tesselin sheets containing Lorem Ipsum passages, and more recently with desktop publishing software like Norvel PageKit including versions of Lorem Ipsum. publishing software like Norvel PageKit including versions of Lorem Ipsum.</p>
  </div>

  <div class="sidebar">
    <p>Lorem Ipsum is<br>simply dummy text<br>of the printing</p>
    <p><span class="lead">Lorem Ipsum is</span><br>simply dummy text</p>
  </div>

  <div class="signature">Marcus Albrecht<br>Managing Director</div>
</section>

<section class="card card-front">
  <div class="footer-band" role="img" aria-label="Decorative red, grey and black wave band across the card"></div>

  <div class="brand"><span class="name">Keller</span><span class="sub">Advisory</span></div>

  <div class="card-contact">
    <div class="addr">P.O. Box 4120 Meridian<br>Idaho 83642</div>
    <ul>
      <li><span>000 0000 00 00</span><span class="ico"></span></li>
      <li><span>000 0000 00 00</span><span class="ico"></span></li>
      <li><span>info@kelleradvisory.com</span><span class="ico"></span></li>
      <li><span>www.<span class="hl">kelleradvisory</span>.com</span><span class="ico"></span></li>
    </ul>
  </div>

  <div class="holder">
    <span class="person">Marcus Albrecht</span>
    <span class="role">Managing Director</span>
  </div>
</section>

<section class="card card-back">
  <div class="brand"><span class="name">Keller</span><span class="sub">Advisory</span></div>
</section>

</body>
</html>
```